Etiketten für Honiggläser gesucht
sehr kreativer Entwurf, in dem alle umfangreichen Vorgaben berücksichtigt wurden. q4712 ist sehr service- und lösungsorientiert. Arbeitet sehr schnell und exzellent.
Zielgruppe
Wir sind eine junge Hobbyimkerei und produzieren unsere eigenen Honigsorten. Zielgruppe ist jeder, der Honig mag.
Aufgabenstellung
Das zu entwerfende Etiketten_Design soll grundsätzlich ein „absoluter Hingucker“ werden, einen hohen Wiedererkennungswert besitzen, edel erscheinen und die Hochwertigkeit des Produktes zum Ausdruck bringen.
Im engeren Sinn sollen zwei voneinander unabhängige Etikettenteile entworfen werden, die aber im Design eine Einheit bilden sollen:
Beim ersten Teil handelt es sich um den sogenannten Gewährverschluss; er verbindet den Deckel mit dem Glas und zerreißt beim ersten Öffnen des Deckels. Der Gewährverschluss soll etwa 2 cm breit und 8 cm lang sein, und unter anderem von unserem Firmenlogo (siehe Datei) geziert werden. Bei dem Logo darf die Grafik und der Hintergrund in der Farbe variieren, und der Schriftzug kann entfallen, andere Änderungen dürfen jedoch nicht vorgenommen werden. Das Logo kann bei Bedarf gerne in anderen Dateiformaten zur Verfügung gestellt werden.
Den zweiten Teil stellt das eigentliche Produktetikett dar. Für dieses gibt es keine Größen- und Formvorgaben, allerdings müssen folgende Inhalte Berücksichtigung finden: Die Daten des Imkers (bitte folgende Platzhalter verwenden „Firmenname“, „Vorname1 & Vorname2 Nachname“, „Straße + Hausnummer“, „PLZ + Ortsname“, „Internetseite“ und „Emailadresse“) sowie den Angaben „500g“, „Mindestens haltbar bis:“ (dahinter oder darunter bitte weißen Freiraum für den Stempelaufdruck des Datums lassen), „Trocken, dunkel und vor Wärme geschützt lagern!“, und – ganz wichtig – die „Honigsorte“ mit den vorangestellten Worten „feinster deutscher“ (, z.B. „feinster deutscher Rapshonig“).
Jede Honigsorte soll mit einer Farbe verknüpft werden, sodass der Kunde schnell erkennen kann um welche Honigsorte es sich im Glas handelt (beispielsweise gelb für Rapshonig, grün für Waldhonig, usw.). Dafür soll die jeweilige Honigsortenfarbe, in welcher Form auch immer, das Etikett oder einen bestimmten Bereich davon domini..

```html
<!DOCTYPE html>
<html lang="de">
<head>
<meta charset="utf-8">
<title>Honigetiketten – Modelle</title>
<link href="https://fonts.googleapis.com/css2?family=Cabin+Condensed:wght@500;600&family=Dancing+Script:wght@500&family=Gochi+Hand&family=Open+Sans:wght@400;600&family=Josefin+Sans:wght@400;600&display=swap" rel="stylesheet">
<style>
  :root {
    --bg: #ffffff;
    --honey-raspberry: #b8154a;
    --ink: #222222;
    --ink-soft: #555555;
    --rule: #333333;
  }
  html, body { margin: 0; padding: 0; overflow: hidden; background: var(--bg); }
  .sheet { display: block; width: 1200px; height: 1200px; }
  .label-frame { fill: none; stroke: var(--honey-raspberry); stroke-width: 5; }
  .label-inner { fill: none; stroke: var(--rule); stroke-width: 0.8; }
  .variety-arc { fill: var(--honey-raspberry); font-family: "Cabin Condensed", sans-serif; font-weight: 600; font-size: 23px; }
  .variety-script { fill: var(--ink); font-family: "Dancing Script", cursive; font-weight: 500; font-size: 25px; }
  .variety-big { fill: var(--honey-raspberry); font-family: "Gochi Hand", cursive; font-size: 32px; letter-spacing: 1px; }
  .address-arc { fill: var(--ink-soft); font-family: "Open Sans", sans-serif; font-size: 10px; }
  .fine-print { fill: var(--ink); font-family: "Open Sans", sans-serif; font-size: 6.8px; }
  .contact { fill: var(--ink); font-family: "Open Sans", sans-serif; font-size: 8.5px; }
  .date-box { fill: #fff; stroke: var(--rule); stroke-width: 0.8; }
  .brand-mark { fill: none; stroke: var(--ink); stroke-width: 3; }
  .brand-name { fill: var(--ink); font-family: "Josefin Sans", sans-serif; font-weight: 400; text-anchor: middle; }
  .brand-top { font-size: 17px; letter-spacing: 5px; }
  .brand-bottom { font-size: 24px; letter-spacing: 2px; }
  .weight { fill: var(--ink); font-family: "Open Sans", sans-serif; font-size: 14px; text-anchor: middle; }
  .model-tag { fill: #000; font-family: "Gochi Hand", cursive; font-size: 36px; font-weight: 700; }
</style>
</head>
<body>
<svg class="sheet" viewBox="0 0 1200 1200" xmlns="http://www.w3.org/2000/svg">
  <defs>
    <path id="arc-a-top" d="M337,231 A165,102 0 0 1 667,231"/>
    <path id="arc-a-bottom" d="M330,231 A172,109 0 0 0 674,231"/>
    <path id="arc-b-top" d="M349,598 A160,100 0 0 1 669,598"/>
    <path id="arc-b-bottom" d="M354,598 A155,103 0 0 0 664,598"/>
    <path id="arc-c-bottom" d="M359,993 A160,100 0 0 0 679,993"/>
  </defs>

  <!-- Modell A -->
  <g class="label label-a">
    <ellipse class="label-frame" cx="502" cy="231" rx="191" ry="125"/>
    <ellipse class="label-inner" cx="502" cy="231" rx="183" ry="118"/>
    <text class="variety-arc"><textPath href="#arc-a-top" startOffset="50%" text-anchor="middle">Feinster deutscher Himbeerhonig</textPath></text>
    <text class="fine-print" x="335" y="221">Trocken, dunkel und vor</text>
    <text class="fine-print" x="335" y="230">Wärme geschützt lagern</text>
    <text class="fine-print" x="597" y="216">Mindestens haltbar bis:</text>
    <rect class="date-box" x="596" y="221" width="74" height="17" rx="2"/>
    <circle class="brand-mark" cx="502" cy="211" r="38"/>
    <text class="brand-name brand-top" x="504" y="274">IMKEREI</text>
    <text class="brand-name brand-bottom" x="503" y="297">RUHNKE</text>
    <text class="weight" x="502" y="321">500G.</text>
    <text class="address-arc"><textPath href="#arc-a-bottom" startOffset="50%" text-anchor="middle">Lindenweg 14 ● 3012 Bern ● www.imkereiruhnke.de ● t@imkereiruhnke.de</textPath></text>
  </g>
  <text class="model-tag" x="800" y="232">Modell A</text>

  <!-- Modell B -->
  <g class="label label-b">
    <ellipse class="label-frame" cx="509" cy="598" rx="191" ry="124"/>
    <ellipse class="label-inner" cx="509" cy="598" rx="183" ry="117"/>
    <text class="variety-script"><textPath href="#arc-b-top" startOffset="50%" text-anchor="middle">feinster deutscher Himbeerhonig</textPath></text>
    <text class="fine-print" x="341" y="589">Trocken, dunkel und vor</text>
    <text class="fine-print" x="341" y="598">Wärme geschützt lagern</text>
    <text class="fine-print" x="341" y="610">Mindestens haltbar bis:</text>
    <rect class="date-box" x="341" y="614" width="74" height="17" rx="2"/>
    <text class="weight" x="377" y="649">500G.</text>
    <g class="contact" text-anchor="end">
      <text x="677" y="580">Lindenweg 14</text>
      <text x="677" y="592">3012 Bern</text>
      <text x="677" y="604">www.imkereiruhnke.de</text>
      <text x="677" y="616">@imkereiruhnke.de</text>
    </g>
    <circle class="brand-mark" cx="509" cy="574" r="38"/>
    <text class="brand-name brand-top" x="511" y="637">IMKEREI</text>
    <text class="brand-name brand-bottom" x="510" y="660">RUHNKE</text>
    <text class="variety-big"><textPath href="#arc-b-bottom" startOffset="50%" text-anchor="middle">Himbeerhonig</textPath></text>
  </g>
  <text class="model-tag" x="795" y="607">Modell B</text>

  <!-- Modell C -->
  <g class="label label-c">
    <ellipse class="label-frame" cx="519" cy="993" rx="191" ry="124"/>
    <ellipse class="label-inner" cx="519" cy="993" rx="183" ry="117"/>
    <text class="fine-print" x="356" y="970">Trocken, dunkel und vor</text>
    <text class="fine-print" x="356" y="979">Wärme geschützt lagern</text>
    <text class="fine-print" x="356" y="990">Mindestens haltbar bis:</text>
    <rect class="date-box" x="356" y="995" width="74" height="17" rx="2"/>
    <g class="contact" text-anchor="end">
      <text x="682" y="966">Lindenweg 14</text>
      <text x="682" y="978">3012 Bern</text>
      <text x="682" y="990">www.imkereiruhnke.de</text>
      <text x="682" y="1002">@imkereiruhnke.de</text>
    </g>
    <circle class="brand-mark" cx="519" cy="946" r="38"/>
    <text class="brand-name brand-top" x="521" y="1009">IMKEREI</text>
    <text class="brand-name brand-bottom" x="520" y="1032">RUHNKE</text>
    <text class="weight" x="521" y="1060">500G.</text>
    <text class="variety-arc"><textPath href="#arc-c-bottom" startOffset="50%" text-anchor="middle">Feinster deutscher Himbeerhonig</textPath></text>
  </g>
  <text class="model-tag" x="793" y="1016">Modell C</text>
</svg>
</body>
</html>
```